Pillow Company needs Pillow Insert Design

I just started a new pillow line with two pillow types. I have a hotel pillow and an organic pillow. I need two pillow insert signs designed that follow the same layout but are different color types. I want one sign to incorporate silver and white look and another sign to incorporate a green and white look (this one to look organic). They must have the same layout but different colors. I have include examples of what I want it to look like. In addition, I have uploaded the two hi res images for each sign. My logo is uploaded too.

I am open to other concepts and colors as long as it looks modern, clean and upscale. In addition, I need a Made in the USA logo on the pillow insert designs.

I have attached details on sign, images to be used, and examples that I like.

The Pillow Sign Size is 12 inches x 12 inches.

```html
<!DOCTYPE html>
<html lang="en">
<head>
<meta charset="utf-8">
<title>LullaLoom Alternative Down Pillow Insert</title>
<link href="https://fonts.googleapis.com/css2?family=Arimo:wght@400;700&display=swap" rel="stylesheet">
<style>
  :root {
    --stage: #8c8c8c;
    --green-top: #9ccd5a;
    --green-mid: #c4e09e;
    --green-pale: #e4efd8;
    --frame: #1b7a3c;
    --brand: #5cb83a;
    --copy: #2b8a2e;
    --note-bg: rgba(70, 140, 70, 0.42);
    --note-text: #1e4a22;
    --white: #ffffff;
    --ink: #111111;
    --badge: #2b3d8c;
  }
  * { margin: 0; padding: 0; box-sizing: border-box; }
  html, body { width: 1200px; height: 1113px; overflow: hidden; }
  body {
    background: radial-gradient(ellipse at center, #a3a3a3 0%, var(--stage) 70%, #777 100%);
    font-family: "Arimo", Arial, sans-serif;
    position: relative;
  }
  .insert {
    position: absolute; left: 82px; top: 38px; width: 1031px; height: 1030px;
    background: linear-gradient(180deg, var(--green-top) 0%, var(--green-mid) 38%, var(--green-pale) 56%, #f2f5ee 100%);
    overflow: hidden;
  }
  .photo {
    position: absolute; left: 0; top: 540px; width: 1031px; height: 490px;
    background: linear-gradient(180deg, rgba(240,242,236,0) 0%, rgba(232,234,228,0.85) 18%, #e6e6e0 45%, #f4f4f2 75%, #fafafa 100%);
  }
  .frame { position: absolute; left: 0; top: 0; }
  .logo-box {
    position: absolute; left: 85px; top: 44px; width: 433px; height: 134px;
    background: var(--white); border: 3px solid var(--frame);
    display: flex; align-items: center;
  }
  .logo-mark { width: 100px; height: 84px; margin-left: 24px; background: var(--brand); }
  .logo-name {
    margin-left: 26px; font-weight: 700; font-size: 44px; color: var(--brand); letter-spacing: -0.5px;
  }
  .title {
    position: absolute; left: 582px; top: 74px;
    color: var(--white); font-weight: 700; font-size: 63px; line-height: 64px;
  }
  .intro {
    position: absolute; left: 67px; top: 205px; width: 520px;
    color: var(--copy); font-size: 19px; line-height: 25.6px;
  }
  .features { position: absolute; left: 67px; top: 341px; list-style: none; }
  .features li {
    display: flex; align-items: center; height: 28.7px;
    color: var(--copy); font-size: 19.5px; white-space: nowrap;
  }
  .features svg { width: 20px; height: 20px; margin-right: 14px; }
  .note {
    position: absolute; left: 575px; top: 295px; width: 456px; height: 107px;
    background: var(--note-bg); color: var(--note-text);
    font-size: 18.5px; line-height: 26px; padding: 13px 0 0 25px;
  }
  .tagline { position: absolute; left: 78px; top: 914px; color: var(--ink); }
  .tagline strong { display: block; font-weight: 400; font-size: 24px; line-height: 28px; }
  .tagline span { display: block; font-size: 18px; line-height: 24px; }
  .origin-badge {
    position: absolute; left: 813px; top: 954px; width: 119px; height: 63px;
    background: var(--badge); border-radius: 4px;
  }
</style>
</head>
<body>
  <section class="insert">
    <div class="photo" role="img" aria-label="Photo of a smiling couple relaxing together on white pillows and bedding in a bright bedroom"></div>

    <svg class="frame" width="1031" height="1030" viewBox="0 0 1031 1030">
      <rect x="42" y="42" width="948" height="946" fill="none" stroke="var(--frame)" stroke-width="4"/>
      <g fill="#2f8a45">
        <rect x="18" y="18" width="48" height="48" transform="rotate(45 42 42)" role="img" aria-label="Corner ornament"/>
        <rect x="966" y="18" width="48" height="48" transform="rotate(45 990 42)" role="img" aria-label="Corner ornament"/>
        <rect x="18" y="964" width="48" height="48" transform="rotate(45 42 988)" role="img" aria-label="Corner ornament"/>
        <rect x="966" y="964" width="48" height="48" transform="rotate(45 990 988)" role="img" aria-label="Corner ornament"/>
      </g>
    </svg>

    <div class="logo-box">
      <div class="logo-mark"></div>
      <div class="logo-name">LullaLoom</div>
    </div>

    <h1 class="title">Alternative<br>Down Pillow</h1>

    <p class="intro">We added revolutionary features from our advanced Super Soft Premium Memory Foam that has an open cell structure design that recovers quickly and does not trap heat to our gel infused polyester fiber to our 100% Certified Organic Cotton Fabric.</p>

    <ul class="features">
      <li><svg viewBox="0 0 20 20"><g fill="var(--frame)"><path d="M10 1l3 4-3 4-3-4z"/><path d="M10 11l3 4-3 4-3-4z"/><path d="M1 10l4-3 4 3-4 3z"/><path d="M11 10l4-3 4 3-4 3z"/></g></svg>Made From the Finest Premium Materials</li>
      <li><svg viewBox="0 0 20 20"><g fill="var(--frame)"><path d="M10 1l3 4-3 4-3-4z"/><path d="M10 11l3 4-3 4-3-4z"/><path d="M1 10l4-3 4 3-4 3z"/><path d="M11 10l4-3 4 3-4 3z"/></g></svg>Adjusts to your Body Weight and Temperature</li>
      <li><svg viewBox="0 0 20 20"><g fill="var(--frame)"><path d="M10 1l3 4-3 4-3-4z"/><path d="M10 11l3 4-3 4-3-4z"/><path d="M1 10l4-3 4 3-4 3z"/><path d="M11 10l4-3 4 3-4 3z"/></g></svg>100% Certified Organic Cotton Fabric</li>
      <li><svg viewBox="0 0 20 20"><g fill="var(--frame)"><path d="M10 1l3 4-3 4-3-4z"/><path d="M10 11l3 4-3 4-3-4z"/><path d="M1 10l4-3 4 3-4 3z"/><path d="M11 10l4-3 4 3-4 3z"/></g></svg>Cool Non-Allergenic, Anti-Microbial, and Hypoallergenic</li>
      <li><svg viewBox="0 0 20 20"><g fill="var(--frame)"><path d="M10 1l3 4-3 4-3-4z"/><path d="M10 11l3 4-3 4-3-4z"/><path d="M1 10l4-3 4 3-4 3z"/><path d="M11 10l4-3 4 3-4 3z"/></g></svg>Conforms to Head and Neck for optimal Alignment during Sleep</li>
      <li><svg viewBox="0 0 20 20"><g fill="var(--frame)"><path d="M10 1l3 4-3 4-3-4z"/><path d="M10 11l3 4-3 4-3-4z"/><path d="M1 10l4-3 4 3-4 3z"/><path d="M11 10l4-3 4 3-4 3z"/></g></svg>Mildew Proof and Dust Mite Resistant</li>
      <li><svg viewBox="0 0 20 20"><g fill="var(--frame)"><path d="M10 1l3 4-3 4-3-4z"/><path d="M10 11l3 4-3 4-3-4z"/><path d="M1 10l4-3 4 3-4 3z"/><path d="M11 10l4-3 4 3-4 3z"/></g></svg>FoamSafe-US ® toxin free certified foam</li>
    </ul>

    <div class="note">This pillow was designed to give you the<br>most comfortable night's sleep in your life.<br>Designed for all types of sleep positions.</div>

    <div class="tagline">
      <strong>Surround Yourself with the Best!</strong>
      <span>Individually Handcrafted and Made in USA</span>
    </div>

    <div class="origin-badge" role="img" aria-label="Made in USA badge"></div>
  </section>
</body>
</html>
```